Tolvane Global Wordpress website design

We need a worddpress website/theme design for a new outsourcing company based in Australia.Name of the company is "Tolvane".
Website content is in progress.
The design needs to be clean without clutter in any section. Some example websites are provided below
Menu
- Resources
- Services
- Our difference
Home page needs to have a gif image, for example http://www.brindleworks.example. or http://www.corvathicket.example or http://www.corvathicket.example/team.html
We like how the corvathicket website flows without having the need to click on the menu. It is also mobile friendly (which is important)
Each piece of content will have a learn more button
A call to action button will be placed on the home page, which will provide our phone number and access to online form*
A call to action button will also be added to various other pages such as Resources.
Resources Section will contain web articles, whitepapers, blog and any other ccontent which helps customer in making a decision
Having the ability to add a video or images on the home page is also important
Ability to edit the content easily via wordpress is extremely important
* This is a great Contact Us form - http://www.pelgrastudio.example/#/schedule-meeting
* We do not need the traditional web form on the contact us page
Target Market(s)
Small to medium businesses requiring outsourcing services
Industry/Entity Type
It Company
Coding
Coded - Design and coding required
Colors
Designer to choose colors to be used in the design.
Look and feel
Each slider illustrates characteristics of the customer's brand and the style your logo design should communicate.

```html
<!DOCTYPE html>
<html lang="en">
<head>
<meta charset="utf-8">
<title>Tolvane — Let's Start</title>
<link rel="stylesheet" href="https://fonts.googleapis.com/css2?family=Open+Sans:wdth,wght@75,700;100,400;100,700&display=swap">
<style>
  :root {
    --ink-white: #ffffff;
    --accent-red: #e8303a;
    --scene-dark: #1f1e1d;
    --scene-mid: #3a3733;
    --scene-warm: #5a4a38;
    --scene-cool: #2b3140;
    --overlay: rgba(10, 10, 12, 0.45);
  }
  * { margin: 0; padding: 0; box-sizing: border-box; }
  html, body { width: 1200px; height: 597px; overflow: hidden; }
  body { font-family: "Open Sans", Arial, sans-serif; color: var(--ink-white); background: var(--scene-dark); }

  .hero { position: relative; width: 1200px; height: 597px; overflow: hidden; }
  .hero-backdrop {
    position: absolute; inset: 0;
    background:
      radial-gradient(ellipse at 45% 35%, rgba(140,140,140,0.35), transparent 55%),
      radial-gradient(ellipse at 62% 72%, rgba(170,110,40,0.35), transparent 40%),
      linear-gradient(100deg, var(--scene-warm) 0%, var(--scene-mid) 35%, var(--scene-mid) 70%, var(--scene-cool) 100%);
  }
  .hero-backdrop::after { content: ""; position: absolute; inset: 0; background: var(--overlay); }

  .brand {
    position: absolute; left: 123px; top: 20px;
    font-size: 46px; font-weight: 400; letter-spacing: 0.16em; line-height: 1;
  }
  .menu-toggle { position: absolute; left: 1059px; top: 35px; }

  .hero-title {
    position: absolute; left: 119px; top: 160px;
    font-stretch: 75%; font-weight: 700; font-size: 60px; line-height: 80px;
    text-transform: uppercase; letter-spacing: 0.01em;
  }
  .hero-lead {
    position: absolute; left: 120px; top: 309px; width: 810px;
    font-size: 15.5px; line-height: 37px;
  }

  .learn-more { position: absolute; left: 123px; top: 418px; display: flex; align-items: center; }
  .learn-more-label { font-size: 10.5px; font-weight: 700; letter-spacing: 0.02em; text-transform: uppercase; }

  .scroll-cue { position: absolute; left: 587px; top: 470px; }

  .copyright { position: absolute; left: 120px; top: 534px; font-size: 12.5px; }
  .social { position: absolute; left: 994px; top: 535px; display: flex; gap: 22px; }
  .social-dot { width: 11px; height: 11px; border-radius: 50%; background: var(--ink-white); }
</style>
</head>
<body>
<section class="hero">
  <div class="hero-backdrop" role="img" aria-label="Photo of a small team meeting around an office table with laptops and coffee cups"></div>

  <div class="brand">TOLVANE</div>

  <svg class="menu-toggle" width="30" height="22" viewBox="0 0 30 22" aria-label="Menu">
    <g stroke="var(--ink-white)" stroke-width="2.6" stroke-linecap="round">
      <line x1="1.5" y1="2" x2="28.5" y2="2"/>
      <line x1="1.5" y1="11" x2="28.5" y2="11"/>
      <line x1="1.5" y1="20" x2="28.5" y2="20"/>
    </g>
  </svg>

  <h1 class="hero-title">Let’s start<br>with Tolvane</h1>

  <p class="hero-lead">Lorem ipsum dolor sit amet, consectetur adipiscing elit. Vivamus id lectus eget mi interdum interdum ut eget turpis. Pellentesque venenatis tellus mi, vitae tristique ante dapibus in.</p>

  <div class="learn-more">
    <span class="learn-more-label">Learn more</span>
    <svg width="186" height="24" viewBox="0 0 186 24" aria-hidden="true">
      <line x1="4" y1="12" x2="164" y2="12" stroke="var(--accent-red)" stroke-width="1.2"/>
      <circle cx="174" cy="12" r="11" fill="var(--accent-red)"/>
      <polyline points="171,7 176,12 171,17" fill="none" stroke="var(--ink-white)" stroke-width="1.8"/>
    </svg>
  </div>

  <svg class="scroll-cue" width="26" height="42" viewBox="0 0 26 42" aria-label="Scroll down">
    <rect x="2" y="1.5" width="22" height="39" rx="11" fill="none" stroke="var(--ink-white)" stroke-width="2"/>
    <line x1="13" y1="8" x2="13" y2="13" stroke="var(--ink-white)" stroke-width="1.6"/>
    <g fill="none" stroke="var(--ink-white)" stroke-width="1.4">
      <polyline points="9,17 13,21 17,17"/>
      <polyline points="9,22 13,26 17,22"/>
      <polyline points="9,27 13,31 17,27"/>
    </g>
  </svg>

  <p class="copyright">Copyright © 2017 Tolvane.</p>

  <div class="social" aria-label="Social links">
    <span class="social-dot"></span>
    <span class="social-dot"></span>
    <span class="social-dot"></span>
  </div>
</section>
</body>
</html>
```